Tovally's Pest Control Billboard

I need a billboard designed for my pest control company. Feel free to check out our website, www.tovallys-example.com. I can also provide any logo, etc for design help. It should be funny but show trust. We want to focus on Mice and rodents. Phone # 555-013-7291 should be used. Shouldn't be to scary, we never use fear to sell.

Target Market(s)

People with pest issues, Mice, Rodents

Industry/Entity Type

Pest Control

Font styles to use
Sans Serif

Colors
59FF00
82FF00
B8FF75
E3FFCB
F4FFEA

Requirements
Must have
• Humor
Nice to have
• Some humor

```html
<!DOCTYPE html>
<html lang="en">
<head>
<meta charset="utf-8">
<title>Tovally's Pest Control Billboard</title>
<link rel="stylesheet" href="https://fonts.googleapis.com/css2?family=Open+Sans:wght@600;700;800&display=swap">
<style>
  :root {
    --page-bg: #e6ecf1;
    --green-deep: #4f961b;
    --green-main: #64a826;
    --green-light: #a3d659;
    --green-band: #9acd48;
    --green-text-dark: #2c5010;
    --green-url: #a9e34d;
    --white: #ffffff;
    --ink: #1e2a14;
    --photo-a: #8f8a7f;
    --photo-b: #7d8a86;
  }
  * { margin: 0; padding: 0; box-sizing: border-box; }
  html, body { width: 1200px; height: 800px; overflow: hidden; }
  body { background: var(--page-bg); font-family: "Open Sans", Arial, sans-serif; }

  .billboard {
    position: absolute; left: 30px; top: 115px; width: 1140px; height: 570px;
    background: linear-gradient(160deg, var(--green-deep), var(--green-main));
    overflow: hidden;
  }
  .brand-swoop { position: absolute; left: 0; top: 0; }
  .brand {
    position: absolute; left: 26px; top: 58px;
    display: flex; align-items: center; gap: 10px;
    font-weight: 700; font-size: 26px; color: var(--ink);
  }
  .brand-dot { width: 16px; height: 16px; border-radius: 50%; background: var(--green-main); }

  .photo { position: absolute; left: 0; width: 168px; }
  .photo--technician { top: 200px; height: 182px; background: linear-gradient(160deg, #b3aea2, var(--photo-a)); }
  .photo--spraying { top: 386px; height: 184px; background: linear-gradient(160deg, #a4b0a8, var(--photo-b)); }

  .headline {
    position: absolute; right: 30px; top: 6px; text-align: right;
    color: var(--white); font-weight: 800; font-size: 96px; line-height: 100px; letter-spacing: -1px;
  }
  .region-badge {
    position: absolute; left: 205px; top: 222px; width: 320px; height: 108px;
    border-radius: 50%; background: var(--green-light);
    display: flex; flex-direction: column; justify-content: center; align-items: center;
    color: var(--white); font-weight: 700; font-size: 31px; line-height: 36px;
  }
  .services { position: absolute; left: 560px; top: 222px; list-style: none; }
  .services li {
    display: flex; align-items: center; gap: 10px;
    color: var(--white); font-weight: 700; font-size: 29px; line-height: 36px;
  }
  .services svg { flex: none; }

  .coverage-band {
    position: absolute; left: 168px; right: 0; top: 340px; height: 78px;
    background: var(--green-band);
    display: flex; flex-direction: column; justify-content: center; align-items: center;
    color: var(--green-text-dark); font-weight: 700; font-size: 21px; line-height: 28px;
  }
  .cta { position: absolute; left: 195px; top: 440px; }
  .cta-main { color: var(--white); font-weight: 700; font-size: 20px; line-height: 28px; }
  .cta-sub { color: var(--green-url); font-weight: 700; font-size: 19px; line-height: 26px; }
  .phone {
    position: absolute; right: 30px; top: 418px;
    color: var(--white); font-weight: 700; font-size: 60px; line-height: 70px;
  }
  .website {
    position: absolute; right: 30px; top: 495px;
    color: var(--green-url); font-weight: 800; font-size: 44px; line-height: 56px;
  }
</style>
</head>
<body>
  <section class="billboard">
    <svg class="brand-swoop" width="420" height="205" viewBox="0 0 420 205" aria-hidden="true">
      <path d="M0 0 H420 C330 70 200 180 0 205 Z" fill="var(--green-light)"/>
      <path d="M0 0 H400 C310 65 190 170 0 192 Z" fill="var(--white)"/>
    </svg>
    <div class="brand"><span class="brand-dot"></span>Tovally's Pest Control</div>

    <div class="photo photo--technician" role="img" aria-label="Technician inspecting a doorway for pests"></div>
    <div class="photo photo--spraying" role="img" aria-label="Technician spraying treatment outside a house"></div>

    <h1 class="headline"><span>YOUR PESTS.</span><br><span>OUR PROBLEM.</span></h1>

    <div class="region-badge"><span>WISCONSIN</span><span>PEST CONTROL</span></div>

    <ul class="services">
      <li><svg width="20" height="20" viewBox="0 0 20 20"><path d="M2 11 L8 17 L18 4" stroke="var(--green-light)" stroke-width="4" fill="none"/></svg>Get Rid of Mice and Rodents</li>
      <li><svg width="20" height="20" viewBox="0 0 20 20"><path d="M2 11 L8 17 L18 4" stroke="var(--green-light)" stroke-width="4" fill="none"/></svg>Eliminate Bugs and Insects</li>
      <li><svg width="20" height="20" viewBox="0 0 20 20"><path d="M2 11 L8 17 L18 4" stroke="var(--green-light)" stroke-width="4" fill="none"/></svg>Effective Pest Management</li>
    </ul>

    <div class="coverage-band">
      <span>Servicing both Residential and Commercial customers</span>
      <span>from Green Bay, Appleton, Brookfield, Sturgeon Bay &amp; Wausau.</span>
    </div>

    <div class="cta">
      <p class="cta-main">CALL A FREE INSPECTION TODAY!</p>
      <p class="cta-sub">One Call, No More Pests!</p>
    </div>
    <p class="phone">(555) 013-7291</p>
    <p class="website">www.tovallys-example.com</p>
  </section>
</body>
</html>
```